Pin Oak Media Outdoor Advertising Corporate Stationery Design

We need a full corporate stationary design for our company Pin Oak Media. We setup and lease billboards, building wraps, trailer ads and construction hoardings.

We need to establish our branding and our newly created logo. All our brand identity should point towards our values, vision and mission.

We are open to fresh new ideas for our stationary design as long as it ultimately reflects the brand & logo.

Corporate Stationary List:
1. Business Card Design
2. Letterhead Design
3. Email Signature Design
4. “Advertise Here” Design (for placement on empty billboards, etc)

All designs must include our logo and be kept simple, modern, friendly and effective.

All designs should please be provided in Illustrator, Photoshop and InDesign file formats.

More details are attached in Word.

Hey

The project has been guaranteed. We like what has been submitted so far but we''d like to see a few concepts for the "Advertise Here" design for open billboards please.

Thanks!

Target Market(s)

Male and female, corporates, business owners, media buying agencies, government & all age groups.

Industry/Entity Type

Construction

Requirements
Must have
• All designs must incorporate our colours: Pantone 319C, 320C, 321C & Hexachrome Black C.

1.Business Card Design
a. Logo
b. Name
c. Mobile
d. Landline
e. Website
f. Facebook
g. Twitter
2. Letterhead Design
a. Logo
b. Mobile
c. Landline
d. Website
e. CC reg number
f. BEE level 4 contributor
g. PRTVA member
h. Postal Address
3. Email Signature Design
a. Logo
b. Name
c. Mobile
d. Landline
e. BEE level 4 contributor
f. PRTVA member
g. Website
h. Facebook
i. Twitter
4. “Advertise Here” Design (for placement on empty billboards, etc) Majority ratio of 2:1 (eg 6m wide by 3m high) - Please use 2 attached photos.
a. Logo .co.za
b. Contact Mirela
c. Mobile
Nice to have
• Come up with a cool slogan / tagline for Business Cards, “Advertise Here” Design

```html
<!DOCTYPE html>
<html lang="en">
<head>
<meta charset="utf-8">
<title>Pin Oak Media — Corporate Stationery</title>
<link rel="stylesheet" href="https://fonts.googleapis.com/css2?family=Barlow+Semi+Condensed:wght@400;500;700&family=Arimo:wght@400&display=swap">
<style>
:root{
  --teal-light:#6ccbd1;
  --teal-mid:#1fa3ad;
  --teal-dark:#0f8892;
  --ink:#1d2527;
  --text:#2b2f31;
  --paper:#ffffff;
  --stage:#e6f1f2;
  --rule:#1d2527;
}
*{margin:0;padding:0;box-sizing:border-box}
html,body{width:1200px;height:950px;overflow:hidden}
body{background:var(--stage);font-family:"Barlow Semi Condensed",Arial,sans-serif;color:var(--text);position:relative}
.sheet{position:absolute;background:var(--paper);box-shadow:0 2px 8px rgba(0,0,0,.12);overflow:hidden}
.brand{display:flex;align-items:center;gap:7px;font-family:"Barlow Semi Condensed",Arial,sans-serif;font-weight:700;color:var(--teal-dark);white-space:nowrap;line-height:1}
.brand-mark{background:var(--teal-dark);flex:none}
.icon{width:9px;height:9px;flex:none;fill:currentColor}
.line{display:flex;align-items:center;gap:5px;white-space:nowrap}
.accent{color:var(--teal-mid)}
.block{position:absolute}

/* Letterhead */
.letterhead{left:30px;top:30px;width:560px;height:890px}
.letterhead .brand{position:absolute;left:36px;top:42px;font-size:26px}
.letterhead .brand-mark{width:22px;height:22px}
.letter-body{position:absolute;left:36px;top:118px;width:488px;font-family:"Arimo",Arial,sans-serif;font-size:11.2px;line-height:1.38;color:var(--text)}
.letter-body p{margin-bottom:14px}
.letter-credentials{position:absolute;right:40px;top:692px;font-size:10px;display:flex;flex-direction:column;gap:3px}
.letter-credentials .icon{color:var(--teal-light)}
.letter-contacts{position:absolute;left:36px;top:770px;font-size:10px;display:flex;flex-direction:column;gap:3px}
.letter-contacts .icon{color:var(--teal-mid)}
.letter-contacts .indent{padding-left:14px}
.letter-band-light{left:210px;bottom:0;width:110px;height:26px;background:var(--teal-light)}
.letter-band-dark{left:326px;bottom:0;width:110px;height:26px;background:var(--teal-dark)}
.letter-band-mid{left:442px;bottom:0;width:118px;height:26px;background:var(--teal-mid)}

/* Business cards */
.card{width:265px;height:152px;top:30px}
.card-front{left:620px}
.card-back{left:905px}
.card-front .brand{position:absolute;left:16px;top:24px;font-size:15px;gap:5px}
.card-front .brand-mark{width:12px;height:12px}
.card-top{left:124px;top:0;width:141px;height:80px;background:var(--teal-light)}
.card-bottom{left:124px;top:86px;width:141px;height:66px;background:var(--teal-mid)}
.card-holder{position:absolute;left:136px;top:26px;color:var(--ink)}
.card-holder .name{font-size:17px;font-weight:700;line-height:1}
.card-holder .role{font-size:9px;margin-top:3px}
.card-direct{position:absolute;left:134px;top:96px;font-size:8px;color:#fff;display:flex;flex-direction:column;gap:4px}
.card-social{position:absolute;left:16px;top:104px;font-size:8px;color:var(--ink);display:flex;flex-direction:column;gap:4px}
.card-social .icon{color:var(--teal-mid)}
.card-back .brand{position:absolute;left:50%;top:50%;transform:translate(-50%,-50%);font-size:28px;gap:8px}
.card-back .brand-mark{width:22px;height:22px}

/* Email signature */
.signature{left:620px;top:207px;width:550px;height:140px}
.signature .rule{position:absolute;left:24px;right:24px;top:24px;height:1.5px;background:var(--rule)}
.signature .brand{position:absolute;left:24px;top:42px;font-size:16px;gap:5px}
.signature .brand-mark{width:12px;height:12px}
.sig-holder{position:absolute;left:160px;top:40px;color:var(--ink)}
.sig-holder .name{font-size:13px;font-weight:700;line-height:1.1}
.sig-holder .role{font-size:10px}
.sig-cols{position:absolute;left:24px;top:86px;display:flex;gap:36px;font-size:9.5px}
.sig-cols .col{display:flex;flex-direction:column;gap:4px}
.sig-cols .icon{color:var(--teal-mid)}

/* Advertise Here board */
.board{left:700px;top:372px;width:390px;height:548px}
.board-band-light{left:0;top:110px;width:200px;height:120px;background:var(--teal-light)}
.board-band-dark{left:200px;top:110px;width:190px;height:120px;background:var(--teal-dark)}
.board-headline{position:absolute;top:152px;font-size:35px;font-weight:700;line-height:1;white-space:nowrap}
.board-headline.advertise{left:24px;color:var(--ink)}
.board-headline.here{left:216px;color:#fff}
.board-contact{position:absolute;left:24px;top:268px;font-size:14px;display:flex;flex-direction:column;gap:4px}
.board-contact .who{color:var(--teal-mid);font-weight:500}
.board-contact .line{color:var(--ink);font-size:13px}
.board-contact .icon{color:var(--teal-mid);width:11px;height:11px}
.board .brand{position:absolute;left:24px;top:440px;font-size:30px;gap:8px}
.board .brand-mark{width:24px;height:24px}
</style>
</head>
<body>

<section class="sheet letterhead" aria-label="Letterhead">
  <div class="brand"><span class="brand-mark"></span>Pin Oak Media</div>

  <div class="letter-body">
    <p>Lorem ipsum dolor sit amet, consectetur adipiscing elit. Mauris viverra tempor metus, quis cursus elit tempor nec. Donec placerat tempus facilisis. Sed enim ante, luctus posuere rutrum eget, cursus rutrum felis. Nullam justo dui, consectetur in sollicitudin eu, dignissim sed leo. Mauris vitae risus odio, vitae mollis nunc. Morbi at ipsum sit amet erat viverra porta quis eu felis. Quisque odio augue, sollicitudin ut hendrerit non, malesuada vel justo. Maecenas dictum, felis sed faucibus egestas, tellus sapien molestie turpis, non fringilla quam orci ac arcu. Suspendisse placerat massa arcu. Proin ligula magna, ultricies suscipit porttitor nec, tincidunt nec fermentum eu, ornare feugiat tellus. Morbi odio accumsan tortor, pharetra lacinia mi urna rhoncus eleifend at, porttitor vel nunc. Class aptent taciti sociosqu inceptos himenaeos. Aenean a felis massa. Curabitur non enim. Nulla facilisi.</p>
    <p>Fusce laoreet posuere dolor. Praesent in ultricies mauris. Fusce laoreet ultricies sit amet. Ut ipsum dui, viverra et rhoncus vel, egestas quis fringilla vel, laoreet vel diam. Aliquam ante nulla dictum erat, quis eleifend leo augue non velit. Etiam sit amet ligula a risus imperdiet aliquet id a risus. Quisque tortor tortor, faucibus sed blandit velit, mattis et vehicula vitae, posuere pulvinar erat. Duis non neque. Etiam bibendum ultricies nunc a dictum. Nunc rutrum blandit erat quis fermentum. Class aptent taciti sociosqu ad litora, per inceptos himenaeos. Duis auctor posuere dapibus. Morbi tincidunt. Duis sem dui, gravida vel ultrices a, tincidunt non ligula. Commodo, enim sem sagittis sem, in posuere mauris turpis eu pulvinar posuere.</p>
    <p>Sed ut risus nec imperdiet. Praesent aliquam porta ligula, ut ornare risus suscipit egestas ultrices. Donec eget mi augue, quis aliquet nisl. Proin ac justo ligula, non blandit elit. Phasellus elementum. In molestie feugiat massa a faucibus. Aenean et tincidunt eros. Suspendisse sit amet lacinia purus. Aenean tincidunt arcu sed massa rhoncus iaculis at nec eros. Maecenas fringilla turpis ut ligula semper egestas rutrum. Ut eget urna erat, ac sodales ipsum. Maecenas fringilla turpis ut ligula semper blandit. Phasellus semper vestibulum mi sed facilisis. Sed luctus ipsum ac sapien elementum ut tristique lacus venenatis.</p>
    <p>Maecenas elementum lacus mauris, id posuere dolor. Praesent in ultricies mauris. Fusce laoreet posuere metus, quis pellentesque tellus ultricies sit amet. Ut ipsum dui, viverra et rhoncus vel, ultricies quis turpis. Aliquam sapien tortor, egestas quis fringilla vel, laoreet vel diam. Aliquam sollicitudin, augue nec molestie adipiscing, ante nulla dictum erat, quis eleifend leo augue non velit. Etiam sit amet ligula a risus imperdiet aliquet id a risus. Quisque tortor tortor, faucibus sed blandit at, pharetra a lorem. Aenean libero velit, mattis et vehicula vitae, posuere pulvinar erat. Duis non</p>
  </div>

  <div class="letter-credentials">
    <div class="line"><svg class="icon" viewBox="0 0 10 10"><rect x="1" y="2" width="8" height="6" rx="1"/></svg><span><span class="accent">CC</span> 2014/3081</span></div>
    <div class="line"><svg class="icon" viewBox="0 0 10 10"><rect x="1.5" y="1.5" width="7" height="7"/></svg><span>BEE <span class="accent">level 4</span> contributor</span></div>
    <div class="line"><svg class="icon" viewBox="0 0 10 10"><circle cx="5" cy="5" r="4"/></svg><span><span class="accent">PRTVA</span> member</span></div>
  </div>

  <div class="letter-contacts">
    <div class="line"><svg class="icon" viewBox="0 0 10 10"><rect x="2.5" y="0.5" width="5" height="9" rx="1"/></svg><span>05 41 3827 1904 55</span></div>
    <div class="line"><svg class="icon" viewBox="0 0 10 10"><path d="M2 1h2l1 2.5-1.2 1a5 5 0 0 0 2.7 2.7l1-1.2L10 7v2a1 1 0 0 1-1 1A8 8 0 0 1 1 2a1 1 0 0 1 1-1z"/></svg><span>12 30 5182 40917</span></div>
    <div class="line"><svg class="icon" viewBox="0 0 10 10"><circle cx="5" cy="5" r="4.2" fill="none" stroke="currentColor" stroke-width="1.2"/><path d="M1 5h8M5 1v8" stroke="currentColor" stroke-width=".8"/></svg><span class="accent">www.pinoakmedia.co.za</span></div>
    <div class="line"><svg class="icon" viewBox="0 0 10 10"><path d="M5 0a3.5 3.5 0 0 1 3.5 3.5C8.5 6 5 10 5 10S1.5 6 1.5 3.5A3.5 3.5 0 0 1 5 0z"/></svg><span>418 Kestrel Road Suite 12</span></div>
    <div class="line indent"><span>Riverton 7700, South Africa</span></div>
  </div>

  <div class="block letter-band-light" aria-hidden="true"></div>
  <div class="block letter-band-dark" aria-hidden="true"></div>
  <div class="block letter-band-mid" aria-hidden="true"></div>
</section>

<section class="sheet card card-front" aria-label="Business card front">
  <div class="block card-top" aria-hidden="true"></div>
  <div class="block card-bottom" aria-hidden="true"></div>
  <div class="brand"><span class="brand-mark"></span>Pin Oak Media</div>
  <div class="card-holder">
    <div class="name">Tomas Vell</div>
    <div class="role">account manager</div>
  </div>
  <div class="card-direct">
    <div class="line"><svg class="icon" viewBox="0 0 10 10"><rect x="2.5" y="0.5" width="5" height="9" rx="1"/></svg><span>05 41 3827 1904 55</span></div>
    <div class="line"><svg class="icon" viewBox="0 0 10 10"><path d="M2 1h2l1 2.5-1.2 1a5 5 0 0 0 2.7 2.7l1-1.2L10 7v2a1 1 0 0 1-1 1A8 8 0 0 1 1 2a1 1 0 0 1 1-1z"/></svg><span>12 30 5182 40917</span></div>
    <div class="line"><svg class="icon" viewBox="0 0 10 10"><rect x="0.5" y="2" width="9" height="6.5" fill="none" stroke="currentColor"/><path d="M0.5 2l4.5 3.5L9.5 2" fill="none" stroke="currentColor"/></svg><span>tomas@pinoakmedia.co.za</span></div>
  </div>
  <div class="card-social">
    <div class="line"><svg class="icon" viewBox="0 0 10 10"><circle cx="5" cy="5" r="3.5"/></svg><span class="accent">pinoakmedia</span></div>
    <div class="line"><svg class="icon" viewBox="0 0 10 10"><circle cx="5" cy="5" r="3.5"/></svg><span class="accent">@pinoakmedia</span></div>
    <div class="line"><svg class="icon" viewBox="0 0 10 10"><circle cx="5" cy="5" r="4.2" fill="none" stroke="currentColor" stroke-width="1.2"/><path d="M1 5h8M5 1v8" stroke="currentColor" stroke-width=".8"/></svg><span>www.<span class="accent">pinoakmedia.co.za</span></span></div>
  </div>
</section>

<section class="sheet card card-back" aria-label="Business card back">
  <div class="brand"><span class="brand-mark"></span>Pin Oak Media</div>
</section>

<section class="sheet signature" aria-label="Email signature">
  <div class="rule"></div>
  <div class="brand"><span class="brand-mark"></span>Pin Oak Media</div>
  <div class="sig-holder">
    <div class="name">Tomas Vell</div>
    <div class="role">account manager</div>
  </div>
  <div class="sig-cols">
    <div class="col">
      <div class="line"><svg class="icon" viewBox="0 0 10 10"><rect x="2.5" y="0.5" width="5" height="9" rx="1"/></svg><span>05 41 3827 1904 55</span></div>
      <div class="line"><svg class="icon" viewBox="0 0 10 10"><path d="M2 1h2l1 2.5-1.2 1a5 5 0 0 0 2.7 2.7l1-1.2L10 7v2a1 1 0 0 1-1 1A8 8 0 0 1 1 2a1 1 0 0 1 1-1z"/></svg><span>12 30 5182 40917</span></div>
    </div>
    <div class="col">
      <div class="line"><svg class="icon" viewBox="0 0 10 10"><rect x="1.5" y="1.5" width="7" height="7"/></svg><span>BEE <span class="accent">level 4</span> contributor</span></div>
      <div class="line"><svg class="icon" viewBox="0 0 10 10"><circle cx="5" cy="5" r="4"/></svg><span><span class="accent">PRTVA</span> member</span></div>
    </div>
    <div class="col">
      <div class="line"><svg class="icon" viewBox="0 0 10 10"><circle cx="5" cy="5" r="3.5"/></svg><span class="accent">pinoakmedia</span></div>
      <div class="line"><svg class="icon" viewBox="0 0 10 10"><circle cx="5" cy="5" r="4.2" fill="none" stroke="currentColor" stroke-width="1.2"/><path d="M1 5h8M5 1v8" stroke="currentColor" stroke-width=".8"/></svg><span>www.<span class="accent">pinoakmedia.co.za</span></span></div>
    </div>
    <div class="col">
      <div class="line"><svg class="icon" viewBox="0 0 10 10"><circle cx="5" cy="5" r="3.5"/></svg><span class="accent">@pinoakmedia</span></div>
    </div>
  </div>
</section>

<section class="sheet board" aria-label="Advertise Here billboard design">
  <div class="block board-band-light" aria-hidden="true"></div>
  <div class="block board-band-dark" aria-hidden="true"></div>
  <div class="board-headline advertise">Advertise</div>
  <div class="board-headline here">Here</div>
  <div class="board-contact">
    <div class="who">Contact Mirela</div>
    <div class="line"><svg class="icon" viewBox="0 0 10 10"><rect x="2.5" y="0.5" width="5" height="9" rx="1"/></svg><span>05 41 3827 1904 55</span></div>
  </div>
  <div class="brand"><span class="brand-mark"></span>Pin Oak Media</div>
</section>

</body>
</html>
```